Business Card Design for company

We want new business cards. We'd like something different-- yet still highly professional. Our tagline is Providing leadership, delivering success. Stock photos are ok, as long as they are relevant and look upscale.

Target Market(s)

Architecture/Business Management Consulting/Engineering Consulting

Contact Information for Business Card

dark gray background with pops of blue might be good, but you tell me. You're the designers. Rounded corners might be nice, but again, you tell me.

Font styles to use
Serif
Sans Serif

Colors
3276b5
5c5c5c
9d9d9d
fbfbfb

Requirements
Nice to have
• Something different, but still very professional.

```html
<!DOCTYPE html>
<html lang="en">
<head>
<meta charset="utf-8">
<title>Business Card – Tagline Side</title>
<link href="https://fonts.googleapis.com/css2?family=Nunito:wght@700;800&display=swap" rel="stylesheet">
<style>
  :root {
    --paper: #f4f5f4;
    --paper-shade: #eceeed;
    --brand-blue: #3283f0;
  }
  html, body {
    margin: 0;
    padding: 0;
    width: 1200px;
    height: 690px;
    overflow: hidden;
  }
  .card {
    position: relative;
    width: 1200px;
    height: 690px;
    background:
      repeating-linear-gradient(177deg, rgba(0,0,0,0.012) 0 2px, rgba(255,255,255,0.02) 2px 5px),
      radial-gradient(ellipse at 50% 50%, var(--paper) 0%, var(--paper-shade) 100%);
  }
  .tagline {
    position: absolute;
    left: 0;
    right: 0;
    top: 322px;
    margin: 0;
    text-align: center;
    font-family: 'Nunito', sans-serif;
    font-weight: 800;
    font-size: 37px;
    line-height: 44px;
    letter-spacing: 1.1px;
    color: var(--brand-blue);
    text-transform: uppercase;
  }
</style>
</head>
<body>
  <main class="card">
    <p class="tagline">Providing leadership, delivering success.</p>
  </main>
</body>
</html>
```